Capital Management company needs a web design

We have a domain name and logo but need hosting and design. Please look at the Must-Haves section.

Target Market(s)

banking industry and investors

Industry/Entity Type

Investment

Coding

Coded - Design and coding required

Number of Pages Required

1 page

Font styles to use
Sans Serif

Requirements
Must have
• Picture(s) of skyscraper skyline (can be of Manhattan, Chicago, or any other major city in the USA).
• Please use the three colors of the logo as a backdrop to part of the webpage(s)
Should not have
• No "what our clients say" section
• No pictures of people

```html
<!DOCTYPE html>
<html lang="en">
<head>
<meta charset="utf-8">
<title>Northbank Capital Management</title>
<link href="https://fonts.googleapis.com/css2?family=Montserrat:wght@300;400;500;600&family=Rubik:wght@400;500;700&display=swap" rel="stylesheet">
<style>
:root{
  --blue:#1a7cc7;
  --blue-dark:#1568a8;
  --grey:#a3a3ac;
  --text:#6f6f78;
  --heading:#7a7a82;
  --white:#ffffff;
  --night:#1c2233;
}
*{margin:0;padding:0;box-sizing:border-box}
html,body{width:1200px;height:3470px;overflow:hidden}
body{position:relative;background:var(--white);font-family:"Montserrat",sans-serif;color:var(--text)}
.abs{position:absolute}

/* header */
.site-header{left:0;top:0;width:1200px;height:95px;background:var(--white)}
.brand{left:75px;top:30px;display:flex;align-items:center;gap:10px}
.brand-mark{width:30px;height:30px;background:var(--blue)}
.brand-name{font-family:"Montserrat",sans-serif;font-weight:600;font-size:15px;line-height:17px;color:var(--blue);text-transform:uppercase;width:140px}
.main-nav{left:440px;top:40px;display:flex;gap:19px;font-size:12px;font-weight:500;text-transform:uppercase;color:#8a8a92}
.main-nav .active{color:var(--blue);border-bottom:2px solid var(--blue);padding-bottom:9px}
.call{left:995px;top:35px;display:flex;align-items:center;gap:10px}
.call-icon{width:30px;height:30px;background:var(--blue);border-radius:3px;display:flex;align-items:center;justify-content:center}
.call small{display:block;font-size:10px;color:#9a9aa2}
.call strong{display:block;font-size:13px;color:var(--blue);font-weight:600}

/* hero */
.hero{left:0;top:95px;width:1200px;height:675px;clip-path:polygon(0 0,100% 0,100% 100%,0 91.5%);
  background:linear-gradient(180deg,#c9d1d8 0%,#8e9aa4 25%,#4b5a68 55%,#2a3340 100%)}
.hero-title{left:0;top:363px;width:1200px;text-align:center;font-family:"Rubik",sans-serif;font-weight:500;font-size:45px;line-height:46px;color:var(--white)}
.hero-btn{left:485px;top:498px;width:235px;height:55px;border:2px solid var(--white);outline:1px solid rgba(255,255,255,.6);outline-offset:3px;color:var(--white);font-family:"Rubik",sans-serif;font-size:14px;font-weight:500;display:flex;align-items:center;justify-content:center;gap:18px}
.arrow{top:410px}
.mouse{left:592px;top:598px;width:16px;height:26px;border:2px solid var(--white);border-radius:8px}
.dots{left:577px;top:691px;display:flex;gap:4px}
.dots span{width:10px;height:8px;border:1.5px solid var(--white);border-radius:4px}

/* intro band */
.intro{left:0;top:710px;width:1200px;height:403px;background:var(--blue);clip-path:polygon(0 0,100% 14.4%,100% 100%,0 100%);z-index:-1}
.intro-title{left:75px;top:864px;font-family:"Rubik",sans-serif;font-weight:700;font-size:28px;line-height:30px;color:var(--white);text-transform:uppercase;white-space:nowrap}
.intro-copy{left:600px;top:866px;width:525px;font-size:14px;line-height:22.5px;color:var(--white)}

/* split sections */
.photo{background:linear-gradient(135deg,#eef1f4,#c9d3dc 50%,#6f8aa3)}
.label{font-family:"Rubik",sans-serif;font-weight:500;font-size:18px;color:var(--blue);text-transform:uppercase}
.lead{font-weight:300;font-size:25px;line-height:36px;color:var(--heading);white-space:nowrap}
.body-copy{font-size:13.5px;line-height:22.5px;color:#7d7d85}
.btn{width:151px;height:43px;background:var(--blue);color:var(--white);font-family:"Rubik",sans-serif;font-size:14px;display:flex;align-items:center;justify-content:center}

/* clients */
.clients{left:0;top:2281px;width:1200px;height:449px;background:var(--grey);clip-path:polygon(0 0,100% 14%,100% 100%,0 100%)}
.section-title{left:0;width:1200px;text-align:center;font-family:"Rubik",sans-serif;font-weight:500;font-size:28px;color:var(--white);text-transform:uppercase}
.client{width:330px;text-align:center;color:var(--white)}
.client h3{font-family:"Rubik",sans-serif;font-weight:500;font-size:17px;text-transform:uppercase;margin-bottom:14px}
.client p{font-size:13.5px;line-height:22.5px}

/* contact */
.contact{left:0;top:2730px;width:1200px;height:516px;clip-path:polygon(0 0,100% 0,100% 100%,0 88.4%);background:linear-gradient(180deg,#2b3244,#1c2233 60%,#161b29)}
.field{background:var(--white);font-size:11px;color:#888;padding:10px 12px}
.submit{left:364px;top:3058px;width:472px;height:43px;background:var(--blue);color:var(--white);font-family:"Rubik",sans-serif;font-weight:500;font-size:14px;display:flex;align-items:center;justify-content:center}

/* footer */
.f-item{display:flex;align-items:center;gap:18px}
.f-item small{display:block;font-size:10px;color:#9a9aa2;text-transform:uppercase}
.f-item strong{display:block;font-size:14px;color:var(--blue);font-weight:500}
.f-small{font-size:10px;color:#9a9aa2}
.social{left:424px;top:3401px;display:flex;gap:6px}
.social span{width:29px;height:29px;border-radius:50%;background:var(--grey)}
.social span.on{background:var(--blue)}
</style>
</head>
<body>

<header class="site-header abs">
  <div class="brand abs"><span class="brand-mark"></span><span class="brand-name">Northbank Capital Management</span></div>
  <nav class="main-nav abs">
    <span class="active">Home</span><span>Who we are</span><span>What we do</span><span>Our clients</span><span>Contact</span>
  </nav>
  <div class="call abs">
    <span class="call-icon"><svg width="16" height="16" viewBox="0 0 24 24"><path fill="#fff" d="M6.6 10.8a15 15 0 0 0 6.6 6.6l2.2-2.2c.3-.3.7-.4 1-.2 1.1.4 2.3.6 3.6.6.6 0 1 .4 1 1V20c0 .6-.4 1-1 1A17 17 0 0 1 3 4c0-.6.4-1 1-1h3.5c.6 0 1 .4 1 1 0 1.3.2 2.5.6 3.6.1.3 0 .7-.2 1z"/></svg></span>
    <div><small>Call us now</small><strong>123-456 7890</strong></div>
  </div>
</header>

<section class="hero abs" role="img" aria-label="Photograph of a city skyscraper skyline beside a river at sunset"></section>
<h1 class="hero-title abs">Lorem Ipsum is simply dummy<br>text of the typeset industry.</h1>
<div class="hero-btn abs">Contact us now <svg width="24" height="10" viewBox="0 0 24 10"><path d="M0 5h22M18 1l4 4-4 4" stroke="#fff" fill="none" stroke-width="1.3"/></svg></div>
<svg class="arrow abs" style="left:48px" width="26" height="46" viewBox="0 0 26 46"><path d="M23 3 4 23l19 20" stroke="#fff" stroke-width="4" fill="none"/></svg>
<svg class="arrow abs" style="left:1126px" width="26" height="46" viewBox="0 0 26 46"><path d="M3 3l19 20L3 43" stroke="#fff" stroke-width="4" fill="none"/></svg>
<div class="mouse abs"></div>
<svg class="abs" style="left:594px;top:632px" width="12" height="8" viewBox="0 0 12 8"><path d="M1 1l5 5 5-5" stroke="#fff" stroke-width="1.5" fill="none"/></svg>
<div class="dots abs"><span></span><span style="background:#fff"></span><span></span></div>

<section class="intro abs"></section>
<h2 class="intro-title abs">Lorem Ipsum is simply<br>dummy text of the printing<br>and typesetting industry<br>Lorem Ipsum has been the<br>industry's standard</h2>
<p class="intro-copy abs">Lorem Ipsum is simply dummy text of the printing and typesetting industry. Lorem Ipsum has been the industry's standard dummy text ever since the 1500s, when an unknown printer took a galley of type and scrambled it to make a type specimen book. It has survived not only five centuries, but also the leap into electronic typesetting, remaining essentially unchanged.</p>

<section class="who">
  <h3 class="label abs" style="left:75px;top:1214px">Who we are</h3>
  <p class="lead abs" style="left:73px;top:1250px">Lorem Ipsum is simply dummy<br>text of the printing and typesetting<br>industry. Lorem Ipsum has been<br>text ever since the 1500s.</p>
  <p class="body-copy abs" style="left:75px;top:1411px;width:465px">Lorem Ipsum is simply dummy text of the printing and typesetting industry. Lorem Ipsum has been the industry's standard dummy text ever since the 1500s, when an unknown printer took a galley of type and scrambled it to make a type specimen book. It has survived not only five centuries, but also the leap into electronic typesetting, remaining essentially unchanged.</p>
  <div class="btn abs" style="left:75px;top:1572px">Contact Us</div>
  <div class="photo abs" style="left:600px;top:1113px;width:600px;height:599px" role="img" aria-label="Photograph of a smartphone showing the website on a desk"></div>
</section>

<section class="what">
  <div class="photo abs" style="left:0;top:1712px;width:600px;height:600px;background:linear-gradient(135deg,#bcd6e2,#a9c7d6 55%,#8fb0c1)" role="img" aria-label="Photograph of a desk with a laptop, notebook and finance sketch"></div>
  <h3 class="label abs" style="left:667px;top:1815px">What we do</h3>
  <p class="lead abs" style="left:665px;top:1850px">Lorem Ipsum is simply dummy<br>text of the printing and typesetting<br>industry. Lorem Ipsum has been<br>text ever since the 1500s.</p>
  <p class="body-copy abs" style="left:667px;top:2011px;width:465px">Lorem Ipsum is simply dummy text of the printing and typesetting industry. Lorem Ipsum has been the industry's standard dummy text ever since the 1500s, when an unknown printer took a galley of type and scrambled it to make a type specimen book. It has survived not only five centuries, but also the leap into electronic typesetting, remaining essentially unchanged.</p>
  <div class="btn abs" style="left:667px;top:2172px">Contact Us</div>
</section>

<section class="clients abs"></section>
<h2 class="section-title abs" style="top:2415px">Our clients</h2>
<div class="client abs" style="left:79px;top:2500px"><h3>Business advisors</h3><p>Lorem Ipsum is simply dummy text of the printing and typesetting industry. Lorem Ipsum has been the industry's standard dummy text ever since the 1500s, when an unknown</p></div>
<div class="client abs" style="left:435px;top:2500px"><h3>Business owners</h3><p>Lorem Ipsum is simply dummy text of the printing and typesetting industry. Lorem Ipsum has been the industry's standard dummy text ever since the 1500s, when an unknown</p></div>
<div class="client abs" style="left:790px;top:2500px"><h3>Investors</h3><p>Lorem Ipsum is simply dummy text of the printing and typesetting industry. Lorem Ipsum has been the industry's standard dummy text ever since the 1500s, when an unknown</p></div>

<section class="contact abs" role="img" aria-label="Photograph of a city skyline at night from above"></section>
<h2 class="section-title abs" style="top:2806px">Contact us</h2>
<div class="field abs" style="left:364px;top:2889px;width:232px;height:34px">First Name</div>
<div class="field abs" style="left:604px;top:2889px;width:232px;height:34px">Last Name</div>
<div class="field abs" style="left:364px;top:2932px;width:232px;height:34px">Phone</div>
<div class="field abs" style="left:604px;top:2932px;width:232px;height:34px">Email</div>
<div class="field abs" style="left:364px;top:2975px;width:472px;height:74px">Message</div>
<div class="submit abs">SUBMIT</div>

<footer>
  <div class="f-item abs" style="left:75px;top:3300px">
    <svg width="24" height="24" viewBox="0 0 24 24"><path fill="#1a7cc7" d="M6.6 10.8a15 15 0 0 0 6.6 6.6l2.2-2.2c.3-.3.7-.4 1-.2 1.1.4 2.3.6 3.6.6.6 0 1 .4 1 1V20c0 .6-.4 1-1 1A17 17 0 0 1 3 4c0-.6.4-1 1-1h3.5c.6 0 1 .4 1 1 0 1.3.2 2.5.6 3.6.1.3 0 .7-.2 1z"/></svg>
    <div><small>Phone</small><strong>123-456 7890</strong></div>
  </div>
  <div class="f-item abs" style="left:424px;top:3300px">
    <svg width="26" height="20" viewBox="0 0 26 20"><rect x="1.5" y="1.5" width="23" height="17" rx="2" fill="none" stroke="#1a7cc7" stroke-width="2"/><path d="M2 3l11 8 11-8" fill="none" stroke="#1a7cc7" stroke-width="2"/></svg>
    <div><small>Email</small><strong>info@northbankcapital.com</strong></div>
  </div>
  <div class="brand abs" style="left:940px;top:3300px"><span class="brand-mark"></span><span class="brand-name">Northbank Capital Management</span></div>
  <span class="f-small abs" style="left:75px;top:3410px">Privacy Policy</span>
  <div class="social abs"><span></span><span class="on"></span><span></span><span></span><span></span></div>
  <span class="f-small abs" style="left:864px;top:3410px">© Copyright 2019 Company Name. All rights reserved.</span>
</footer>

</body>
</html>
```